Business Card for Multi-Brand Sportswear Company

We are looking for a business card which represents our company and the multiple brands within it.

The company: Kelt Athletic (LTD)
The brands: Kelt, PawaLuni, VerdantFlex, Grit and Gale

Employees using these cards would be representing Kelt Athletic, rather than any of the individual brands. You will see a current design within the uploaded files, to give some inspiration. The actual text of the brands is not necessary, but the logos should be on there is some format.

Our creative minds on this are stretched, so we are looking for someone to make this their own, and show us what a good business card should look like.

We may like to get these printed with spot gloss, so keep that in mind with your designs.

www.keltathletic.co.uk

Industry/Entity Type

Business

Contact Information for Business Card

Tom Hollingsworth-Pryce
Operations Manager
(+44) 1632 960 418
Tom@keltathletic.co.uk
www.keltathletic.co.uk

Font styles to use
Sans Serif
Other font styles liked:
• Eurostile

Colors
ffffff

Requirements
Nice to have
• Dark (black) background

```html
<!DOCTYPE html>
<html lang="en">
<head>
<meta charset="utf-8">
<title>Kelt Athletic – Business Card</title>
<link href="https://fonts.googleapis.com/css2?family=Michroma&family=Open+Sans:wght@400;600&display=swap" rel="stylesheet">
<style>
  :root {
    --backdrop: #2e2825;
    --card: #1c1c1d;
    --card-edge: #121213;
    --ink: #e6e6e6;
    --ink-soft: #b9b9b9;
    --ink-muted: #8a8a8a;
    --accent: #e3262b;
    --stripe-white: #ffffff;
    --badge-plum: #6d5a80;
    --badge-silver: #cfcfcf;
    --badge-coral: #e85a50;
    --badge-white: #f2f2f2;
  }
  * { box-sizing: border-box; margin: 0; padding: 0; }
  html, body { width: 1200px; height: 716px; overflow: hidden; }
  body {
    background: var(--backdrop);
    font-family: "Open Sans", Arial, sans-serif;
    position: relative;
  }
  .card {
    position: absolute;
    top: 203px;
    width: 540px;
    height: 310px;
    background: radial-gradient(ellipse at 40% 30%, #262627 0%, var(--card) 60%, var(--card-edge) 100%);
    overflow: hidden;
    box-shadow: 0 10px 30px rgba(0,0,0,.45);
  }
  .card--front { left: 40px; }
  .card--back { left: 620px; }

  .card__stripe {
    position: absolute;
    left: 0; right: 0; bottom: 14px;
    height: 9px;
    background: linear-gradient(100deg, var(--accent) 0 52%, var(--stripe-white) 52% 100%);
  }

  .brand-lockup { position: absolute; text-align: left; }
  .card--front .brand-lockup { left: 130px; top: 88px; }
  .card--back .brand-lockup { left: 34px; top: 30px; transform: scale(.72); transform-origin: top left; }

  .brand-lockup__name {
    display: flex;
    align-items: center;
    gap: 10px;
    font-family: "Michroma", "Open Sans", sans-serif;
    font-size: 24px;
    color: var(--ink);
    letter-spacing: 1px;
  }
  .brand-lockup__mark {
    width: 14px; height: 14px;
    background: var(--accent);
  }
  .brand-lockup__rule {
    height: 2px;
    width: 280px;
    background: #4a4a4a;
    margin: 8px 0 10px;
  }
  .brand-badges { display: flex; gap: 22px; margin-left: 4px; }
  .brand-badge {
    width: 34px; height: 26px;
    border-radius: 3px;
  }
  .brand-badge--pawaluni { background: var(--badge-plum); }
  .brand-badge--verdantflex { background: var(--badge-silver); }
  .brand-badge--grit-gale { background: var(--badge-coral); }
  .brand-badge--kelt { background: var(--badge-white); }
  .brand-lockup__company {
    margin-top: 10px;
    font-family: "Michroma", "Open Sans", sans-serif;
    font-size: 11px;
    letter-spacing: 7px;
    color: var(--ink-soft);
  }

  .contact-person { position: absolute; left: 40px; top: 150px; }
  .contact-person__name { font-size: 17px; font-weight: 600; color: var(--ink); }
  .contact-person__role { font-size: 12px; color: var(--ink-muted); margin: 2px 0 0 48px; }

  .contact-details {
    position: absolute;
    left: 330px; top: 150px;
    font-size: 13px;
    line-height: 1.45;
    color: var(--ink-soft);
  }
  .contact-details__web { letter-spacing: 2px; margin-bottom: 18px; }
  .contact-details__address { margin-bottom: 12px; }
</style>
</head>
<body>
  <section class="card card--front">
    <div class="brand-lockup">
      <div class="brand-lockup__name"><span class="brand-lockup__mark"></span>KELT ATHLETIC</div>
      <div class="brand-lockup__rule"></div>
      <div class="brand-badges">
        <span class="brand-badge brand-badge--pawaluni" aria-label="PawaLuni"></span>
        <span class="brand-badge brand-badge--verdantflex" aria-label="VerdantFlex"></span>
        <span class="brand-badge brand-badge--grit-gale" aria-label="Grit and Gale"></span>
        <span class="brand-badge brand-badge--kelt" aria-label="Kelt"></span>
      </div>
      <div class="brand-lockup__company">KELT ATHLETIC (LTD)</div>
    </div>
    <div class="card__stripe"></div>
  </section>

  <section class="card card--back">
    <div class="brand-lockup">
      <div class="brand-lockup__name"><span class="brand-lockup__mark"></span>KELT ATHLETIC</div>
      <div class="brand-lockup__rule"></div>
      <div class="brand-badges">
        <span class="brand-badge brand-badge--pawaluni" aria-label="PawaLuni"></span>
        <span class="brand-badge brand-badge--verdantflex" aria-label="VerdantFlex"></span>
        <span class="brand-badge brand-badge--grit-gale" aria-label="Grit and Gale"></span>
        <span class="brand-badge brand-badge--kelt" aria-label="Kelt"></span>
      </div>
      <div class="brand-lockup__company">KELT ATHLETIC (LTD)</div>
    </div>

    <div class="contact-person">
      <div class="contact-person__name">Tom Hollingsworth-Pryce</div>
      <div class="contact-person__role">Operations Manager</div>
    </div>

    <div class="contact-details">
      <div class="contact-details__web">www.keltathletic.co.uk</div>
      <div class="contact-details__address">Harrow Mill, Kelby,<br>Northallerton, DL9 8ZX</div>
      <div>(+44) 1632 960 418</div>
      <div>Tom@keltathletic.co.uk</div>
    </div>
    <div class="card__stripe"></div>
  </section>
</body>
</html>
```